Velmora Handel Stationary
Simple
Jonas Brückler
Co-Founder
Velmora Handel UG
Lindenkamp 12
48213 Falkenried
Germany
jonas.brueckler@velmora-handel.example
www.velmora-handel.example
Please use the some font as in the logo and work out a proposal based on the red and yellow logo in the uploaded rar file. Whether or not you use the globe in the back (you will see in the rar file) is up to you. The corporate slogan 'Your gateway to infinite opportunities' can be integrated but it's not a must.
Corporate Logo (with or without slogan, up to you)
Please refer to the logos. Ideally work sth out from the colorful version (red and yellow) with or without the globe in the back. You will see when looking at the file.

```html
<!DOCTYPE html>
<html lang="de">
<head>
<meta charset="utf-8">
<title>Velmora Handel Stationary</title>
<link href="https://fonts.googleapis.com/css2?family=Arimo:wght@400;700&display=swap" rel="stylesheet">
<style>
  :root {
    --page: #ffffff;
    --frame: #9a9a9a;
    --card-edge: #3a3a3a;
    --red-deep: #7e0d16;
    --red-mid: #b8202b;
    --red-light: #d8434b;
    --brand-red: #c0222c;
    --ink: #4a4a4a;
    --orange-core: #ffd04a;
    --orange-mid: #fbb82c;
    --orange-edge: #f29a12;
    --white: #ffffff;
  }
  * { margin: 0; padding: 0; box-sizing: border-box; }
  html, body { width: 1200px; height: 670px; overflow: hidden; background: var(--page); }
  body { font-family: "Arimo", Arial, sans-serif; position: relative; }
  .sheet-frame {
    position: absolute; inset: 4px;
    border: 2px solid var(--frame);
  }
  .card {
    position: absolute; top: 199px; width: 473px; height: 269px;
    overflow: hidden; border: 1px solid var(--card-edge);
  }
  .card--front { left: 115px; background: var(--white); }
  .card--back {
    left: 607px; width: 502px; border-color: transparent;
    background: radial-gradient(ellipse at 55% 50%, var(--orange-core) 0%, var(--orange-mid) 45%, var(--orange-edge) 100%);
  }
  .front-swoosh { position: absolute; inset: 0; }
  .brand {
    position: absolute; left: 22px; top: 18px;
    display: flex; flex-direction: column; align-items: center;
  }
  .brand__dot {
    width: 44px; height: 44px; border-radius: 50%;
    background: var(--brand-red);
  }
  .brand__name {
    margin-top: 6px; color: var(--brand-red);
    font-weight: 700; font-size: 22px; letter-spacing: 1px;
  }
  .holder {
    position: absolute; left: 268px; top: 18px; color: var(--white);
  }
  .holder__name { font-size: 21px; font-weight: 400; line-height: 1.1; }
  .holder__role { font-size: 17px; font-weight: 400; line-height: 1.1; }
  .contact {
    position: absolute; left: 0; right: 0; top: 182px;
    text-align: center; color: var(--ink); font-style: normal;
    font-size: 10.5px; line-height: 15px;
  }
  .contact .gap { margin-top: 6px; }
  .back-brand {
    position: absolute; left: 50%; top: 50%; transform: translate(-50%, -50%);
    display: flex; flex-direction: column; align-items: center; gap: 10px;
  }
  .back-brand__dot {
    width: 96px; height: 96px; border-radius: 50%; background: var(--brand-red);
  }
  .back-brand__name {
    color: var(--brand-red); font-weight: 700; font-size: 26px; letter-spacing: 1px;
  }
</style>
</head>
<body>
  <div class="sheet-frame"></div>

  <section class="card card--front">
    <svg class="front-swoosh" width="473" height="269" viewBox="0 0 473 269">
      <defs>
        <radialGradient id="swooshRed" cx="0.7" cy="0.35" r="0.7">
          <stop offset="0" stop-color="#d8434b"/>
          <stop offset="0.55" stop-color="#b8202b"/>
          <stop offset="1" stop-color="#7e0d16"/>
        </radialGradient>
      </defs>
      <path d="M105 0 C150 70 250 150 473 165 L473 0 Z" fill="url(#swooshRed)"/>
    </svg>

    <div class="brand">
      <div class="brand__dot"></div>
      <div class="brand__name">VELMORA</div>
    </div>

    <div class="holder">
      <div class="holder__name">Jonas Brückler</div>
      <div class="holder__role">Co-Founder</div>
    </div>

    <address class="contact">
      <div>Velmora Handel UG Lindenkamp 12</div>
      <div>48213 Falkenried Germany</div>
      <div class="gap">Phone: +49 5731 4417 - 20 &nbsp;Cell: +49 151 26 43 9052</div>
      <div>Email: jonas.brueckler@velmora-handel.example www.velmora-handel.example</div>
    </address>
  </section>

  <section class="card card--back">
    <div class="back-brand">
      <div class="back-brand__dot"></div>
      <div class="back-brand__name">VELMORA</div>
    </div>
  </section>
</body>
</html>
```